Lumen! Consulting

We need a web design for a new supply chain consulting business. we will work with major brands in the electronics, apparel, toy and jewelry industries to create a sustainability program for our customers and implement in their supply chain. We want our customers to have confidence in their supply chain responsibility program. We also manage stakeholder engagements, NGO relationships, and external communications.

I would like to colors to be green, orange and/or black to match the logo (attached). The final design should communicate positive and optimistic leadership - for a professional, sustainable, business.

Industry/Entity Type

Business

```html
<!DOCTYPE html>
<html lang="en">
<head>
<meta charset="utf-8">
<title>Lumen! Consulting</title>
<link rel="stylesheet" href="https://fonts.googleapis.com/css2?family=Oswald:wght@300;400&family=Arimo:wght@400;700&display=swap">
<style>
:root{
  --orange:#f4a123;
  --green:#7dc242;
  --dark:#222222;
  --footer:#363636;
  --page:#efefef;
  --white:#ffffff;
  --text:#555555;
  --heading:#1d1d1d;
}
*{margin:0;padding:0;box-sizing:border-box}
html,body{width:922px;height:1200px;overflow:hidden;background:var(--page)}
body{font-family:"Arimo",Arial,sans-serif;color:var(--text);position:relative}
.display{font-family:"Oswald","Arial Narrow",sans-serif;font-weight:400}
.abs{position:absolute}

/* header */
.site-header{left:0;top:0;width:922px;height:100px;background:var(--dark)}
.brand{left:70px;top:30px;display:flex;align-items:center;gap:8px}
.brand-dot{width:22px;height:22px;border-radius:50%;background:var(--orange)}
.brand-name{font-family:"Oswald",sans-serif;font-weight:300;font-size:30px;color:var(--orange);letter-spacing:1px}
.main-nav{left:288px;top:0;height:100px;display:flex;list-style:none}
.main-nav li{height:100px;display:flex;align-items:center;padding:0 16px;font-family:"Oswald",sans-serif;font-size:15.5px;color:#f2f2f2;font-weight:300}
.main-nav li.active{background:var(--orange);width:81px;justify-content:center;padding:0}

/* hero */
.hero{left:0;top:100px;width:922px;height:241px;background:linear-gradient(90deg,#5fb98e 0%,#bfe6d6 35%,#d8efe4 55%,#8fd060 100%)}
.hero-visual{left:560px;top:100px;width:362px;height:241px;background:linear-gradient(135deg,#f6c31c 0%,#6fcf2a 35%,#2f9b5e 60%,#5cc31f 85%,#f6c31c 100%)}
.hero-copy{left:68px;top:155px;width:272px}
.hero-copy h1{font-family:"Oswald",sans-serif;font-weight:400;font-size:19.5px;line-height:26px;color:var(--heading);letter-spacing:.4px}
.hero-copy p{font-size:11.2px;line-height:17.6px;color:#3d5a4c;margin-top:6px;width:270px}

/* welcome */
.welcome-title{left:0;top:352px;width:922px;text-align:center;font-size:20px;color:var(--orange)}
.welcome-photo{left:59px;top:388px;width:376px;height:187px;background:linear-gradient(120deg,#3a3a3a,#9a9a9a 50%,#e6e6e6 70%,#4a4a4a)}
.welcome-text{left:445px;top:385px;width:400px;font-size:10.3px;line-height:17.6px;color:var(--text)}
.welcome-text p+p{margin-top:17.6px}

/* service cards */
.service{top:593px;width:257px;height:200px;background:var(--white);text-align:center}
.service svg{margin-top:22px}
.service h2{font-size:19px;color:var(--orange);margin-top:2px}
.service p{text-align:left;font-size:10px;line-height:17.6px;padding:0 2px 0 9px;margin-top:4px}

/* news */
.news{left:59px;top:812px;width:396px;height:184px;background:var(--white);padding:4px 8px 0 8px}
.news h2{font-size:19px;color:var(--orange);padding-left:1px}
.news-item{border-bottom:1px dotted #9cc86d;padding:0 0 4px 0}
.news-item h3{font-size:11.5px;font-weight:700;color:#444;line-height:16px}
.news-item p{font-size:10.3px;line-height:13.6px;margin-top:2px}
.read-more{display:block;text-align:right;font-family:"Oswald",sans-serif;font-size:13px;color:var(--orange);text-decoration:underline;line-height:16px}

/* highlights */
.highlights{left:481px;top:812px;width:396px;height:184px;background:var(--white)}
.highlight{height:56px;display:grid;grid-template-columns:54px 90px 244px;align-items:center;border-bottom:1px solid #e6e6e6}
.highlight:last-child{border-bottom:none}
.highlight .icon{display:flex;justify-content:center;padding-left:16px}
.highlight h3{font-size:19px;color:var(--orange);padding-left:15px;white-space:nowrap}
.highlight p{font-size:10.3px;line-height:13.8px;color:#333}

/* footer */
.site-footer{left:0;top:1012px;width:922px;height:161px;background:var(--footer)}
.footer-nav{left:69px;list-style:none}
.footer-nav li{font-family:"Oswald",sans-serif;font-weight:300;font-size:14px;line-height:21.6px;color:#f2f2f2}
.footer-nav li.active{color:var(--orange)}
.footer-col{top:1016px}
.footer-col h2{font-size:19px;color:var(--orange);font-weight:300}
.footer-col p{font-size:10.3px;line-height:17.6px;color:#eeeeee}
.social{display:grid;grid-template-columns:repeat(4,30px);gap:17px 15px;margin-top:10px;padding-left:4px}
.social span{width:30px;height:30px;border-radius:50%;background:var(--orange);border:2px solid #e8e8e8;display:block}
.copyright{left:0;top:1173px;width:922px;height:27px;line-height:27px;text-align:center;font-size:9.5px;color:#222;background:var(--page)}
.copyright b{color:var(--orange);font-weight:400;text-decoration:underline}
</style>
</head>
<body>

<header class="site-header abs"></header>
<div class="brand abs"><span class="brand-dot"></span><span class="brand-name">Lumen!</span></div>
<ul class="main-nav abs">
  <li class="active">Home</li><li>About</li><li>Clients</li><li>Capabilities</li><li>Industries</li><li>Experience</li><li>Contact</li>
</ul>

<section class="hero abs"></section>
<div class="hero-visual abs" role="img" aria-label="Collage of green and yellow diamond tiles showing apparel, a smartphone, a camera, jewelry and a toy"></div>
<div class="hero-copy abs">
  <h1>Lorem Ipsum is simply dummy text of the printing and typesetting .</h1>
  <p>Lorem Ipsum is simply dummy text of the printing and typesetting industry. Lorem Ipsum has been the industry's standard dummy text ever since the 1500s</p>
</div>

<h2 class="welcome-title display abs">Welcome to LUMEN Supply Chain Management</h2>
<div class="welcome-photo abs" role="img" aria-label="Photo of a business team reviewing documents at a meeting table"></div>
<div class="welcome-text abs">
  <p>Lorem Ipsum is simply dummy text of the printing and typesetting industry. Lorem Ipsum has been the industry's standard dummy text ever since the 1500s, when an unknown printer took a galley of type and scrambled it to make a type specimen book. It has survived not only five centuries, but also the leap into electronic typesetting, remaining essentially unchanged. It was popularised in the 1960s with the release of Glyphset sheets containing Lorem Ipsum passages, and more recently with desktop publishing software like Pressline DeskWriter including versions of Lorem Ipsum.</p>
  <p>Lorem Ipsum is simply dummy text of the printing and typesetting industry. Lorem Ipsum has been the industry's standard dummy text ever since the 1500s, when an unknown printer took a galley of type and scrambled it to make a type specimen book.</p>
</div>

<article class="service abs" style="left:60px">
  <svg width="56" height="48" viewBox="0 0 56 48" aria-hidden="true"><g fill="#7dc242"><rect x="22" y="0" width="12" height="12" rx="2"/><rect x="26" y="12" width="4" height="10"/><rect x="8" y="20" width="40" height="4"/><rect x="8" y="20" width="4" height="14"/><rect x="26" y="20" width="4" height="14"/><rect x="44" y="20" width="4" height="14"/><rect x="3" y="34" width="13" height="13" rx="2"/><rect x="21" y="34" width="13" height="13" rx="2"/><rect x="39" y="34" width="13" height="13" rx="2"/></g></svg>
  <h2 class="display">Stakeholder Engagements</h2>
  <p>Lorem Ipsum is simply dummy text of the printing and typesetting industry. Lorem Ipsum has been the industry's standard dummy text ever since the 1500s, when an unknown printer took a galley of type...</p>
</article>
<article class="service abs" style="left:341px">
  <svg width="56" height="48" viewBox="0 0 56 48" aria-hidden="true"><g fill="#f4a123"><circle cx="12" cy="10" r="6"/><circle cx="44" cy="10" r="6"/><path d="M1 30a11 9 0 0 1 22 0z"/><path d="M33 30a11 9 0 0 1 22 0z"/><circle cx="28" cy="16" r="9"/><path d="M12 48v-8a16 12 0 0 1 32 0v8z"/></g></svg>
  <h2 class="display">NGO Relationships</h2>
  <p>Lorem Ipsum is simply dummy text of the printing and typesetting industry. Lorem Ipsum has been the industry's standard dummy text ever since the 1500s, when an unknown printer took a galley of type...</p>
</article>
<article class="service abs" style="left:621px">
  <svg width="56" height="48" viewBox="0 0 56 48" aria-hidden="true"><g fill="none" stroke="#7dc242" stroke-width="6"><rect x="8" y="3" width="16" height="24" rx="8" transform="rotate(-40 16 15)"/><rect x="30" y="21" width="16" height="24" rx="8" transform="rotate(-40 38 33)"/><line x1="22" y1="20" x2="32" y2="28"/></g></svg>
  <h2 class="display">External Communications</h2>
  <p>Lorem Ipsum is simply dummy text of the printing and typesetting industry. Lorem Ipsum has been the industry's standard dummy text ever since the 1500s, when an unknown printer took a galley of type...</p>
</article>

<section class="news abs">
  <h2 class="display">Latest News</h2>
  <div class="news-item">
    <h3>Lorem Ipsum is simply dummy text of the printing industry.</h3>
    <p>Lorem Ipsum is simply dummy text of the printing and typesetting industry. Lorem Ipsum has been the industry's standard dummy text ever since the 1500s...</p>
    <span class="read-more">Read More</span>
  </div>
  <div class="news-item" style="margin-top:6px">
    <h3>Lorem Ipsum is simply dummy text of the printing industry.</h3>
    <p>Lorem Ipsum is simply dummy text of the printing and typesetting industry. Lorem Ipsum has been the industry's standard dummy text ever since the 1500s...</p>
    <span class="read-more">Read More</span>
  </div>
</section>

<section class="highlights abs">
  <div class="highlight">
    <span class="icon"><svg width="24" height="34" viewBox="0 0 24 34" aria-hidden="true"><path d="M12 2a10 10 0 0 0-6 18v5h12v-5A10 10 0 0 0 12 2z" fill="none" stroke="#f4a123" stroke-width="2.5"/><rect x="7" y="27" width="10" height="3" fill="#f4a123"/><rect x="9" y="31" width="6" height="2.5" fill="#f4a123"/></svg></span>
    <h3 class="display">Challange</h3>
    <p>Lorem Ipsum is simply dummy text of the printing and typesetting industry. Lorem Ipsum has been the industry's standard dummy text ever since the 1500s</p>
  </div>
  <div class="highlight">
    <span class="icon"><svg width="26" height="34" viewBox="0 0 26 34" aria-hidden="true"><rect x="2" y="2" width="22" height="30" fill="none" stroke="#f4a123" stroke-width="2.5"/><g fill="#f4a123"><rect x="6" y="6" width="3" height="3"/><rect x="11.5" y="6" width="3" height="3"/><rect x="17" y="6" width="3" height="3"/><rect x="6" y="12" width="3" height="3"/><rect x="11.5" y="12" width="3" height="3"/><rect x="17" y="12" width="3" height="3"/><rect x="6" y="18" width="3" height="3"/><rect x="11.5" y="18" width="3" height="3"/><rect x="17" y="18" width="3" height="3"/><rect x="10" y="25" width="6" height="7"/></g></svg></span>
    <h3 class="display">Industry</h3>
    <p>Lorem Ipsum is simply dummy text of the printing and typesetting industry. Lorem Ipsum has been the industry's standard dummy text ever since the 1500s</p>
  </div>
  <div class="highlight">
    <span class="icon"><svg width="34" height="26" viewBox="0 0 34 26" aria-hidden="true"><path d="M4 22C6 8 18 2 32 3c0 12-8 20-22 18z" fill="#f4a123"/><path d="M2 25C10 16 18 11 26 8" stroke="#ffffff" stroke-width="2" fill="none"/></svg></span>
    <h3 class="display">Expertise</h3>
    <p>Lorem Ipsum is simply dummy text of the printing and typesetting industry. Lorem Ipsum has been the industry's standard dummy text ever since the 1500s</p>
  </div>
</section>

<footer class="site-footer abs"></footer>
<ul class="footer-nav abs" style="top:1016px">
  <li class="active">Home</li><li>About</li><li>Clients</li><li>Capabilities</li><li>Industries</li><li>Experience</li><li>Contact</li>
</ul>
<div class="footer-col abs" style="left:265px;width:190px">
  <h2 class="display">How can we help</h2>
  <p>Lorem Ipsum is simply dummy text of the printing and typesetting industry. Lorem Ipsum has been the industry's standard dummy text ever since 1500s</p>
  <p style="margin-top:17.6px">Lorem Ipsum is simply dummy text of the printing and typesetting industry.</p>
</div>
<div class="footer-col abs" style="left:471px;width:190px">
  <h2 class="display">Get in Touch With Us</h2>
  <p style="padding-left:2px">Office no., Area name<br>City, State, Country<br>Call : +44 100 200 3000<br>Fax : +44 100 200 3001<br>Email : info@lumenconsult.com<br>Support : support@lumenconsult.com</p>
</div>
<div class="footer-col abs" style="left:672px;width:190px">
  <h2 class="display">Follow Us</h2>
  <div class="social" aria-label="Social media links">
    <span></span><span></span><span></span><span></span>
    <span></span><span></span><span></span><span></span>
  </div>
</div>

<div class="copyright abs">© <b>LUMEN </b> - 2014. All Rights Reserved.</div>

</body>
</html>
```